Banner Designs for Field Keep Ad Campaign

Harrowmere is a security consulting and services company that offers a service called FieldKeepUnit. FieldKeepUnit helps our customers secure large events by providing rapidly deployable security and communications technologies in a Field Keep vehicle, on a per event basis. We are looking for a designer to create a banner ad in three sizes for our campaign.
Target Market(s)
Our campaign is geared to the sports and entertainment industry, specifically large event venues and their security operation.
Industry/Entity Type
Security
Font styles to use
Other font styles liked:
- Raleway
Requirements
Must have
- Banner Objective
The visual and textual content of the banner should prompt the viewer to quickly identify the service offered and the information that is available to download.
Banner Design
Logo: FieldKeepUnit logo
Call to Action Button in Red: Get Details (On Right or or Upper Right)
Title in Larger Font: Take Control of you Events
Subtitle in smaller Font: Your Force Multiplier - Field Keep as a Service
Background: Photo of Field Keep interior or exterior or photo of female operator.
Font: Raleway
Banner Sizes
1 - 1200x670 pixels
2 - 1510x196 pixels
3 - 1200x628 pixels
Nice to have
- Follow the look and feel of the samples provided.

```html
<!DOCTYPE html>
<html lang="en">
<head>
<meta charset="utf-8">
<title>FieldKeepUnit Banner Set</title>
<link href="https://fonts.googleapis.com/css2?family=Raleway:wght@500;600;800;900&display=swap" rel="stylesheet">
<style>
  :root {
    --page-bg: #93c4f2;
    --navy-deep: #041426;
    --navy: #0b1f35;
    --title-blue: #2f73bd;
    --white: #ffffff;
    --ribbon-red: #e00a0a;
    --skin-light: #b08a6c;
    --skin: #87644e;
    --skin-shade: #4a3a34;
    --hair: #8c7d62;
    --room-dark: #16212f;
  }
  * { margin: 0; padding: 0; box-sizing: border-box; }
  html, body {
    width: 1051px; height: 1200px; overflow: hidden;
    background: var(--page-bg);
    font-family: 'Raleway', sans-serif;
  }
  .canvas { position: relative; width: 1051px; height: 1200px; }
  .banner {
    position: absolute; overflow: hidden;
    background: linear-gradient(100deg, var(--navy-deep) 0%, var(--navy) 50%, var(--navy-deep) 100%);
  }
  .banner--large { left: 154px; top: 61px; width: 744px; height: 415px; }
  .banner--leaderboard { left: 58px; top: 539px; width: 936px; height: 122px; }
  .banner--social { left: 154px; top: 725px; width: 744px; height: 389px; }

  .operator-photo {
    position: absolute; top: 0; right: 0; height: 100%;
    background:
      linear-gradient(90deg, var(--navy) 0%, rgba(11,31,53,0.85) 12%, rgba(11,31,53,0) 38%),
      linear-gradient(180deg, rgba(0,0,0,0) 70%, rgba(10,20,32,0.45) 100%),
      radial-gradient(ellipse 55% 35% at 70% 6%, var(--hair) 0%, rgba(140,125,98,0) 100%),
      radial-gradient(ellipse 62% 80% at 58% 58%, var(--skin-light) 0%, var(--skin) 38%, var(--skin-shade) 68%, var(--room-dark) 100%);
  }
  .banner--large .operator-photo, .banner--social .operator-photo { width: 400px; }
  .banner--leaderboard .operator-photo { width: 290px; }

  .brand { position: absolute; color: var(--white); font-weight: 500; }
  .brand__name { display: block; line-height: 1; }
  .brand__by { display: block; text-align: right; line-height: 1; font-weight: 600; }

  .banner--large .brand, .banner--social .brand { left: 38px; top: 124px; width: 270px; }
  .banner--large .brand { top: 66px; }
  .banner--social .brand { top: 66px; }
  .banner--large .brand__name, .banner--social .brand__name { font-size: 35px; }
  .banner--large .brand__by, .banner--social .brand__by { font-size: 14px; margin-top: 5px; }

  .banner--leaderboard .brand { left: 38px; top: 50px; width: 190px; }
  .banner--leaderboard .brand__name { font-size: 25px; }
  .banner--leaderboard .brand__by { font-size: 10px; margin-top: 3px; }

  .headline {
    position: absolute; color: var(--title-blue);
    font-weight: 900; text-transform: uppercase; letter-spacing: -0.5px;
  }
  .banner--large .headline, .banner--social .headline {
    left: 36px; font-size: 46px; line-height: 55px;
  }
  .banner--large .headline { top: 167px; }
  .banner--social .headline { top: 153px; }
  .banner--leaderboard .headline {
    left: 290px; width: 322px; top: 14px; text-align: center;
    font-size: 30px; line-height: 35px;
  }

  .subhead { position: absolute; color: var(--white); font-weight: 600; }
  .banner--large .subhead, .banner--social .subhead {
    left: 38px; width: 330px; font-size: 21px; line-height: 27px;
  }
  .banner--large .subhead { top: 294px; }
  .banner--social .subhead { top: 282px; }
  .banner--leaderboard .subhead {
    left: 255px; width: 402px; top: 87px; text-align: center;
    font-size: 13px; font-weight: 500;
  }

  .ribbon { position: absolute; top: 0; right: 0; }
  .ribbon text {
    fill: var(--white); font-family: 'Raleway', sans-serif;
    font-weight: 800; text-transform: uppercase;
  }
</style>
</head>
<body>
<div class="canvas">

  <section class="banner banner--large">
    <div class="operator-photo" role="img" aria-label="Photo of a female security operator with a headset in a dark control room"></div>
    <div class="brand"><span class="brand__name">FieldKeepUnit</span><span class="brand__by">By Harrowmere</span></div>
    <h1 class="headline">Take Control<br>of You Events</h1>
    <p class="subhead">Your Force Multiplier - Field Keep as a Service</p>
    <svg class="ribbon" width="130" height="130" viewBox="0 0 130 130">
      <polygon points="0,0 65,0 130,65 130,130" fill="var(--ribbon-red)"/>
      <text x="0" y="0" font-size="19" transform="translate(80 50) rotate(45)" text-anchor="middle" dominant-baseline="middle">Get Details</text>
    </svg>
  </section>

  <section class="banner banner--leaderboard">
    <div class="operator-photo" role="img" aria-label="Photo of a female security operator with a headset in a control room"></div>
    <div class="brand"><span class="brand__name">FieldKeepUnit</span><span class="brand__by">By Harrowmere</span></div>
    <h2 class="headline">Take Control of<br>You Events</h2>
    <p class="subhead">Your Force Multiplier - Field Keep as a Service</p>
    <svg class="ribbon" width="112" height="112" viewBox="0 0 112 112">
      <polygon points="0,0 64,0 112,48 112,112" fill="var(--ribbon-red)"/>
      <text x="0" y="0" font-size="15" transform="translate(70 41) rotate(45)" text-anchor="middle" dominant-baseline="middle">Get Details</text>
    </svg>
  </section>

  <section class="banner banner--social">
    <div class="operator-photo" role="img" aria-label="Photo of a female security operator with a headset in a dark control room"></div>
    <div class="brand"><span class="brand__name">FieldKeepUnit</span><span class="brand__by">By Harrowmere</span></div>
    <h2 class="headline">Take Control<br>of You Events</h2>
    <p class="subhead">Your Force Multiplier - Field Keep as a Service</p>
    <svg class="ribbon" width="130" height="130" viewBox="0 0 130 130">
      <polygon points="0,0 65,0 130,65 130,130" fill="var(--ribbon-red)"/>
      <text x="0" y="0" font-size="19" transform="translate(80 50) rotate(45)" text-anchor="middle" dominant-baseline="middle">Get Details</text>
    </svg>
  </section>

</div>
</body>
</html>
```